Lantern Quay Mentoring seeks to be a Guidance Counsellor to the World

Word Press site to be published to HostMerry account on completion.

Basic site with integration wth Vexo Word Press Plug-in.

All simple pages to create are shown in attached power point.

LanternQuayMentoring.example™️ seeks to be a Guidance Counsellor to the World. We help students by bringing high quality, interactive content to their virtual doorstep.

Target Market(s)

Careers

Font styles to use
Sans Serif

Requirements
Must have
• Details are in powerpoint:
Registration to allow integration with Word Press Vexo Plug-in.
Nice to have
• Bright and modern feel

```html
<!DOCTYPE html>
<html lang="en">
<head>
<meta charset="utf-8">
<title>Lantern Quay Mentoring – Town Hall</title>
<link href="https://fonts.googleapis.com/css2?family=Fira+Sans:wght@400;500;600;700;800&family=Poppins:wght@800&display=swap" rel="stylesheet">
<style>
  :root{
    --stage:#58585a;
    --orange:#f7941d;
    --ink:#1d1d1f;
    --slate:#4a4a4c;
    --title-grey:#6f7073;
    --concrete-top:#e4e5e6;
    --concrete-mid:#eef0f1;
    --concrete-low:#d3dde3;
    --floor-top:#5c7484;
    --floor-bottom:#3d5566;
    --footer-dark:#1c2830;
    --card:#ffffff;
    --button-dark:#3f3f42;
  }
  *{box-sizing:border-box;margin:0;padding:0}
  html,body{width:970px;height:1200px;overflow:hidden}
  body{background:var(--stage);font-family:"Fira Sans",Arial,sans-serif;position:relative}

  .page{position:absolute;left:54px;width:856px;height:521px;overflow:hidden;
    background:linear-gradient(180deg,var(--concrete-top) 0%,var(--concrete-mid) 45%,var(--concrete-low) 100%);}
  .page--event{top:51px}
  .page--programs{top:622px}

  .brand{position:absolute;left:94px;top:46px;display:flex;align-items:center;gap:8px}
  .brand__dot{width:18px;height:18px;border-radius:50%;background:var(--orange)}
  .brand__name{font-weight:600;font-size:17px;color:var(--slate);line-height:1.1;width:140px}

  .nav{position:absolute;top:18px;left:0;width:100%;height:22px}
  .nav__item{position:absolute;top:0;height:22px;line-height:22px;font-size:11px;font-weight:600;color:var(--ink);letter-spacing:.2px;white-space:nowrap}
  .nav__item--mission{left:418px}
  .nav__item--programs{left:508px}
  .nav__item--involved{left:617px}
  .nav__item--info{left:720px;display:flex;align-items:center;gap:4px}
  .nav__item--active{left:503px;width:95px;text-align:center;background:var(--orange);color:#fff}

  .event__kicker{position:absolute;left:94px;top:186px;font-size:14px;font-weight:500;color:var(--slate)}
  .event__title{position:absolute;left:94px;top:208px;font-size:31px;font-weight:800;color:var(--orange);letter-spacing:.6px;white-space:nowrap}
  .speaker{position:absolute;left:96px;top:269px;width:199px;height:56px;border:1px solid var(--orange);padding:11px 0 0 13px}
  .speaker__name{font-size:13.5px;font-weight:600;color:var(--slate);letter-spacing:.2px}
  .speaker__role{font-size:10.5px;color:var(--slate);margin-top:1px}
  .event__tagline{position:absolute;left:93px;top:357px;font-family:"Poppins",sans-serif;font-weight:800;font-size:24.5px;line-height:34px;color:var(--title-grey);letter-spacing:-.3px}

  .event__illustration{position:absolute;left:448px;top:83px;width:285px;height:438px;
    background:radial-gradient(ellipse at 45% 15%,#fff7e0 0%,#d9dadb 35%,rgba(200,205,210,0) 70%),
    linear-gradient(180deg,rgba(0,0,0,0) 50%,rgba(60,80,110,.35) 100%)}

  .floor{position:absolute;left:0;top:459px;width:100%;height:62px;background:linear-gradient(180deg,var(--floor-top),var(--floor-bottom))}
  .floor::before{content:"";position:absolute;left:0;top:0;width:100%;height:5px;background:#3b4f5c}
  .footer-bar{position:absolute;left:0;top:474px;width:100%;height:47px;background:var(--footer-dark)}
  .copyright{position:absolute;left:95px;font-size:8.5px;color:#fff}
  .page--event .copyright{top:490px}
  .page--programs .copyright{top:494px}

  .speakers{position:absolute;left:94px;top:167px;display:flex;gap:7px}
  .speaker-card{width:161px;height:257px;background:var(--card);border-radius:2px;position:relative}
  .speaker-card__photo{height:140px;width:100%}
  .speaker-card__photo--one{background:linear-gradient(135deg,#8b7a62,#c9b9a5 60%,#7a8f90)}
  .speaker-card__photo--two{background:linear-gradient(135deg,#4b5258,#a8adb2 60%,#d5d7da)}
  .speaker-card__photo--three{background:linear-gradient(135deg,#16c6d6,#1bb7c7 50%,#6b7a8e)}
  .speaker-card__photo--four{background:linear-gradient(135deg,#6d7378,#b9bdc0 50%,#2b7a45)}
  .speaker-card__name{position:absolute;left:15px;top:151px;font-size:9.5px;font-weight:600;color:var(--ink);letter-spacing:.2px}
  .btn{position:absolute;left:15px;font-size:7.5px;font-weight:700;letter-spacing:.2px;text-align:center;line-height:17px;height:17px}
  .btn--bio{top:171px;width:47px;border:1px solid var(--orange);color:var(--orange);line-height:15px}
  .btn--register{top:203px;width:74px;background:var(--orange);color:#fff}
  .btn--calendar{top:225px;width:84px;background:var(--button-dark);color:#fff}
</style>
</head>
<body>

<section class="page page--event">
  <div class="brand"><span class="brand__dot"></span><span class="brand__name">Lantern Quay Mentoring</span></div>
  <nav class="nav">
    <span class="nav__item nav__item--mission">OUR MISSION</span>
    <span class="nav__item nav__item--programs">OUR PROGRAMS</span>
    <span class="nav__item nav__item--involved">GET INVOLVED</span>
    <span class="nav__item nav__item--info">INFO <svg width="8" height="6" viewBox="0 0 8 6"><path d="M1 1l3 3 3-3" fill="none" stroke="#1d1d1f" stroke-width="1.4"/></svg></span>
  </nav>
  <p class="event__kicker">TOWN HALL:</p>
  <h1 class="event__title">“WAR ON VIRUSES”</h1>
  <div class="speaker">
    <p class="speaker__name">DR. MIRELA CONWAY, PHD</p>
    <p class="speaker__role">Senior Research Scientist</p>
  </div>
  <h2 class="event__tagline">THE WORLD’S GUIDANCE<br>COUNSELLOR</h2>
  <div class="floor"></div>
  <div class="event__illustration" role="img" aria-label="Photo of a woman seated on a chair looking up at a glowing light bulb surrounded by sketched idea doodles"></div>
  <p class="copyright">Copyright © 2020 All Rights Reserved</p>
</section>

<section class="page page--programs">
  <div class="brand"><span class="brand__dot"></span><span class="brand__name">Lantern Quay Mentoring</span></div>
  <nav class="nav">
    <span class="nav__item nav__item--mission">OUR MISSION</span>
    <span class="nav__item nav__item--active">OUR PROGRAMS</span>
    <span class="nav__item nav__item--involved">GET INVOLVED</span>
    <span class="nav__item nav__item--info">INFO <svg width="8" height="6" viewBox="0 0 8 6"><path d="M1 1l3 3 3-3" fill="none" stroke="#1d1d1f" stroke-width="1.4"/></svg></span>
  </nav>

  <div class="speakers">
    <article class="speaker-card">
      <div class="speaker-card__photo speaker-card__photo--one" role="img" aria-label="Portrait photo of speaker Mirela Conway"></div>
      <h3 class="speaker-card__name">MIRELA CONWAY</h3>
      <span class="btn btn--bio">VIEW BIO</span>
      <span class="btn btn--register">REGISTER NOW</span>
      <span class="btn btn--calendar">ADD TO CALENDAR</span>
    </article>
    <article class="speaker-card">
      <div class="speaker-card__photo speaker-card__photo--two" role="img" aria-label="Portrait photo of speaker Petra Lindqvist"></div>
      <h3 class="speaker-card__name">PETRA LINDQVIST</h3>
      <span class="btn btn--bio">VIEW BIO</span>
      <span class="btn btn--register">REGISTER NOW</span>
      <span class="btn btn--calendar">ADD TO CALENDAR</span>
    </article>
    <article class="speaker-card">
      <div class="speaker-card__photo speaker-card__photo--three" role="img" aria-label="Portrait photo of speaker Jonah Abernathy"></div>
      <h3 class="speaker-card__name">JONAH ABERNATHY</h3>
      <span class="btn btn--bio">VIEW BIO</span>
      <span class="btn btn--register">REGISTER NOW</span>
      <span class="btn btn--calendar">ADD TO CALENDAR</span>
    </article>
    <article class="speaker-card">
      <div class="speaker-card__photo speaker-card__photo--four" role="img" aria-label="Portrait photo of speaker Renata Okafor"></div>
      <h3 class="speaker-card__name">RENATA OKAFOR</h3>
      <span class="btn btn--bio">VIEW BIO</span>
      <span class="btn btn--register">REGISTER NOW</span>
      <span class="btn btn--calendar">ADD TO CALENDAR</span>
    </article>
  </div>

  <div class="footer-bar"></div>
  <p class="copyright">Copyright © 2020 All Rights Reserved</p>
</section>

</body>
</html>
```